Briefpapier für Träger der Familienhilfe
Sie geht auf alle Wünsche sehr schnell ein!! Sehr gute Zusammenarbeit! Danke
Zielgruppe
Wir sind ein Träger der Familienhilfe und bieten Hilfen zur Erziehung an. Unsere Auftraggeber sind die Jugendämter in Hamburg. Unsere Zielgruppe sind Familien/Einzelpersonen in Krisensituationen.
Aufgabenstellung
Wir möchten, dass unser Logo in das Design integriert wird. Da der Briefverkehr hauptsächlich mit Behörden, Ämtern, Schulen etc. stattfinden wird, ist es wichtig, dass wir einen seriösen Eindruck machen.

```html
<!DOCTYPE html>
<html lang="de">
<head>
<meta charset="utf-8">
<title>Lumen Familienhilfe – Briefpapier</title>
<link rel="stylesheet" href="https://fonts.googleapis.com/css2?family=Open+Sans:wght@400;700&display=swap">
<style>
:root{
  --stage:#6b6969;
  --paper:#ffffff;
  --green:#9bc537;
  --grey-text:#8c8c8c;
  --ink:#2b2b2b;
  --faint:#f3f3f3;
  --window:#f1f1f1;
}
*{margin:0;padding:0;box-sizing:border-box}
html,body{width:1200px;height:539px;overflow:hidden;background:var(--stage);font-family:"Open Sans",sans-serif;color:var(--ink)}
.board{position:relative;width:1200px;height:539px}
.letterhead{position:absolute;top:24px;width:348px;height:492px;background:var(--paper);box-shadow:0 0 14px rgba(0,0,0,.35)}
.letterhead::after{content:"";position:absolute;right:0;top:0;width:5px;height:100%;background:var(--green)}
.letterhead--first{left:32px}
.letterhead--second{left:415px}
.brand{position:absolute;left:146px;top:12px;display:flex;align-items:flex-start;gap:4px;color:var(--grey-text)}
.brand__dot{width:11px;height:11px;border-radius:50%;background:var(--green);margin-top:3px}
.brand__name{font-size:18px;line-height:20px;font-weight:400}
.brand__name small{display:block;font-size:9.5px;line-height:11px}
.sender-line{position:absolute;left:34px;top:85px;font-size:3px;text-decoration:underline;white-space:nowrap}
.sender-line span{color:var(--green)}
.contact{position:absolute;left:253px;top:86px;border-left:.6px solid #aaa;padding-left:6px;font-size:4.6px;line-height:6.5px}
.contact__address{margin-bottom:3px}
.contact__row{display:flex;align-items:center;gap:3px}
.contact__row svg{width:4.5px;height:4.5px;fill:var(--green)}
.fold-mark{position:absolute;left:0;width:10px;height:.6px;background:#bbb}
.watermark{position:absolute;left:122px;top:266px;width:110px;height:110px;border-radius:50%;background:var(--faint)}
.footer{position:absolute;left:36px;top:458px;display:flex;font-size:4.6px;line-height:6.5px}
.footer__col{padding-right:9px}
.footer__col+.footer__col{border-left:.6px solid var(--green);padding-left:9px}
.footer__col:nth-child(1){width:78px}
.footer__col:nth-child(2){width:108px}
.envelope{position:absolute;left:801px;width:364px;height:182px;background:var(--paper);box-shadow:0 0 14px rgba(0,0,0,.35);overflow:hidden}
.envelope--back{top:133px}
.envelope--front{top:334px}
.envelope__flap{position:absolute;left:0;top:0;width:364px;height:55px}
.envelope__return{position:absolute;left:0;right:0;top:165px;text-align:center;font-size:4.5px}
.envelope__return span{color:var(--green)}
.envelope .brand{left:38px;top:8px}
.envelope__window{position:absolute;left:41px;top:83px;width:149px;height:75px;border-radius:6px;background:var(--window);border:.6px solid #d6d6d6}
.envelope .watermark{left:260px;top:20px;width:90px;height:90px}
</style>
</head>
<body>
<div class="board">

  <section class="letterhead letterhead--first">
    <div class="brand"><span class="brand__dot"></span><div class="brand__name">Lumen<small>Familienhilfe</small></div></div>
    <p class="sender-line">Lumen Familienhilfe UG <span>|</span> Lindenweg 14 <span>|</span> 22305 Hamburg</p>
    <div class="contact">
      <p class="contact__address">Lumen Familienhilfe UG<br>Lindenweg 14<br>22305 Hamburg</p>
      <p class="contact__row"><svg viewBox="0 0 10 10"><path d="M2 1l2 2-1 1.5c.8 1.5 1.8 2.5 3 3L7.5 6l2 2-1.5 1.5C4.5 9 1 5.5.5 2z"/></svg>040 31 72 84 10</p>
      <p class="contact__row"><svg viewBox="0 0 10 10"><rect x="1" y="3" width="8" height="5" rx="1"/><rect x="3" y="1" width="4" height="2"/></svg>040 31 72 84 12</p>
      <p class="contact__row"><svg viewBox="0 0 10 10"><rect x="0.5" y="2" width="9" height="6"/></svg>info@lumen-familienhilfe.de</p>
      <p class="contact__row"><svg viewBox="0 0 10 10"><circle cx="5" cy="5" r="4.5"/></svg>www.lumen-familienhilfe.de</p>
    </div>
    <span class="fold-mark" style="top:164px"></span>
    <span class="fold-mark" style="top:328px"></span>
    <div class="watermark" role="img" aria-label="Dezentes Markenzeichen im Hintergrund"></div>
    <div class="footer">
      <div class="footer__col"><b>Inhaber:</b> Mara Beispiel<br>Lindenweg 14<br>22305 Hamburg</div>
      <div class="footer__col">Amtsgericht Ulm<br><b>Steuerliche ID:</b> De418270050<br><b>Umsatzsteuer ID:</b> 47 120 386 000</div>
      <div class="footer__col"><b>Nordbank Berlin</b><br><b>BIC:</b> NRDBDEFF000<br><b>IBAN:</b> DE41 2105 0170 0012 3456 78</div>
    </div>
  </section>

  <section class="letterhead letterhead--second">
    <div class="brand"><span class="brand__dot"></span><div class="brand__name">Lumen<small>Familienhilfe</small></div></div>
    <p class="sender-line">Lumen Familienhilfe UG <span>|</span> Lindenweg 14 <span>|</span> 22305 Hamburg</p>
    <div class="contact">
      <p class="contact__address">Lumen Familienhilfe UG<br>Lindenweg 14<br>22305 Hamburg</p>
      <p class="contact__row"><svg viewBox="0 0 10 10"><path d="M2 1l2 2-1 1.5c.8 1.5 1.8 2.5 3 3L7.5 6l2 2-1.5 1.5C4.5 9 1 5.5.5 2z"/></svg>040 31 72 84 10</p>
      <p class="contact__row"><svg viewBox="0 0 10 10"><rect x="1" y="3" width="8" height="5" rx="1"/><rect x="3" y="1" width="4" height="2"/></svg>040 31 72 84 12</p>
      <p class="contact__row"><svg viewBox="0 0 10 10"><rect x="0.5" y="2" width="9" height="6"/></svg>info@lumen-familienhilfe.de</p>
      <p class="contact__row"><svg viewBox="0 0 10 10"><circle cx="5" cy="5" r="4.5"/></svg>www.lumen-familienhilfe.de</p>
    </div>
    <span class="fold-mark" style="top:164px"></span>
    <span class="fold-mark" style="top:328px"></span>
    <div class="footer">
      <div class="footer__col"><b>Inhaber:</b> Mara Beispiel<br>Lindenweg 14<br>22305 Hamburg</div>
      <div class="footer__col">Amtsgericht Ulm<br><b>Steuerliche ID:</b> De418270050<br><b>Umsatzsteuer ID:</b> 47 120 386 000</div>
      <div class="footer__col"><b>Nordbank Berlin</b><br><b>BIC:</b> NRDBDEFF000<br><b>IBAN:</b> DE41 2105 0170 0012 3456 78</div>
    </div>
  </section>

  <section class="envelope envelope--back">
    <svg class="envelope__flap" viewBox="0 0 364 55" aria-hidden="true">
      <path d="M0 0H364L349 47Q346 55 338 55H26Q18 55 16 48Z" fill="var(--green)"/>
      <circle cx="180" cy="12" r="4" fill="#fff"/>
    </svg>
    <p class="envelope__return">Lumen Familienhilfe UG <span>|</span> Lindenweg 14 <span>|</span> 22305 Hamburg</p>
  </section>

  <section class="envelope envelope--front">
    <div class="watermark" role="img" aria-label="Dezentes Markenzeichen im Hintergrund"></div>
    <div class="brand"><span class="brand__dot"></span><div class="brand__name">Lumen<small>Familienhilfe</small></div></div>
    <div class="envelope__window"></div>
  </section>

</div>
</body>
</html>
```